Marisol business card and stationary
business card and stationary
Marisol business card and stationary - Retailers
Creative Brief
Bright & Fun-filled
Janet Wroblenko
owner, designer
marisol a florist 418 north brook lane greenville, sc 29174
info@marisolblooms.example
marisolblooms.example
Concepts
Stationery for Online Retailer

```html
<!DOCTYPE html>
<html lang="en">
<head>
<meta charset="utf-8">
<title>Marisol – Business Card</title>
<link href="https://fonts.googleapis.com/css2?family=Open+Sans:wght@400;600;700&display=swap" rel="stylesheet">
<style>
  :root {
    --page-bg: #e6e4e0;
    --card-light: #fdf5e2;
    --card-warm: #f7dfc4;
    --olive: #7d8a2c;
    --olive-dark: #66721f;
    --ink: #4a4037;
    --ink-soft: #5e554b;
    --cream-text: #fbf3dc;
    --accent: #e06a78;
  }
  * { margin: 0; padding: 0; box-sizing: border-box; }
  html, body {
    width: 1200px; height: 892px; overflow: hidden;
    background: var(--page-bg);
    font-family: "Open Sans", Arial, sans-serif;
  }
  .stage { position: relative; width: 1200px; height: 892px; }

  .card {
    position: absolute;
    width: 620px; height: 354px;
    border-radius: 18px;
    overflow: hidden;
    background: radial-gradient(ellipse at 40% 40%, var(--card-light) 0%, var(--card-light) 45%, var(--card-warm) 100%);
    box-shadow: 0 10px 26px rgba(0,0,0,0.22);
  }
  .card--front { left: 80px; top: 70px; }
  .card--back { left: 500px; top: 462px; }

  /* Wordmark */
  .wordmark {
    position: absolute;
    display: flex; align-items: center; gap: 12px;
    color: var(--ink);
    font-weight: 600;
    letter-spacing: -0.5px;
  }
  .wordmark__dot {
    border-radius: 50%;
    background: var(--accent);
    flex: none;
  }
  .card--front .wordmark { left: 150px; top: 112px; font-size: 60px; }
  .card--front .wordmark__dot { width: 26px; height: 26px; }
  .card--back .wordmark { left: 46px; top: 128px; font-size: 42px; }
  .card--back .wordmark__dot { width: 18px; height: 18px; }

  .front-band {
    position: absolute; left: 0; right: 0; bottom: 0;
    height: 62px;
    background: var(--olive);
    display: flex; align-items: center; justify-content: center;
  }
  .front-band__web {
    color: var(--cream-text);
    font-size: 22px;
    font-weight: 600;
    letter-spacing: 3px;
  }

  .back-ribbon {
    position: absolute; left: 92px; top: 0;
    width: 70px; height: 48px;
    background: var(--olive);
  }

  .contact {
    position: absolute; left: 340px; top: 76px;
    color: var(--ink-soft);
  }
  .contact__name {
    color: var(--olive);
    font-size: 26px; font-weight: 700;
    line-height: 1.2;
  }
  .contact__role {
    color: var(--ink);
    font-size: 21px; font-weight: 400;
    margin-bottom: 24px;
  }
  .contact__address,
  .contact__lines {
    font-size: 14.5px; line-height: 1.45;
  }
  .contact__address { margin-bottom: 22px; }
  .contact__lines b { font-weight: 700; color: var(--ink); }
</style>
</head>
<body>
<main class="stage">

  <section class="card card--front" aria-label="Business card front">
    <div class="wordmark">
      <span class="wordmark__dot"></span>
      <span class="wordmark__name">marisol</span>
    </div>
    <div class="front-band">
      <span class="front-band__web">www.marisolblooms.example</span>
    </div>
  </section>

  <section class="card card--back" aria-label="Business card back">
    <div class="back-ribbon"></div>
    <div class="wordmark">
      <span class="wordmark__dot"></span>
      <span class="wordmark__name">marisol</span>
    </div>
    <div class="contact">
      <p class="contact__name">Janet Wroblenko</p>
      <p class="contact__role">owner, designer</p>
      <p class="contact__address">marisol a florist<br>418 north brook lane<br>greenville, sc 29174</p>
      <p class="contact__lines">
        <b>P :</b> 864.555.0148<br>
        <b>E :</b> info@marisolblooms.example<br>
        www.marisolblooms.example
      </p>
    </div>
  </section>

</main>
</body>
</html>
```